Microsoft Word Sales Proposal Template

We'd like to produce a standard sales proposal template for Microsoft Word that better represents our company than our current template. Right now we have a very basic, dated look and feel to our template. We would like a proposal that graphically reflects our current branding, cleanly communicates the information contained in the proposal, and keeps the reader visually engaged with the text.

Our proposal documents consistently include the following hierarchy of information. We’d like a template designed to be flexible to change in this hierarchy, with a focus on cohesive design elements (heading fonts and styling, etc.):

- Cover Page
- Table of Contents
- Executive Summary
- Project Approach
- Sample Work/Select Clients List
- About Wexmoor Lane
- References
- Project Milestones and Budget
- Appendices

The primary focus is on the visual design elements: headers and footers, fonts, heading design consistency, and other graph and visual elements reflected in the attached proposal samples.

The Wexmoor Lane logo should not be altered in any way. I have attached 2 acceptable logos for use in the document. Client logos should also not be altered in any way. Placeholders for client logos in the template are appreciated for speed and accuracy of placement. Please avoid using cheesy stock photos.

For more information about our company and to review our current aesthetic, please visit http://www.wexmoorlane.com/.
Updates

Thanks to everyone who has saved the project. We're excited to see your work. Please reach out if you need any clarifications or have questions.

Target Market(s)

Employees at large nonprofits who are responsible for technology decisions. Also target employees who create content and manage content for nonprofits.

Industry/Entity Type

It Company

Font styles to use
Serif
Sans Serif

Requirements
Must have
• Must Have:
• - Sample Table of Content
• - Representation of Section Headings
• - Clean design representative of our brand
• - Template elements that appropriately reflect each potential Table of Contents item
• - Easy flow of reading
• - Templates for reusable graphs and tables
• - Include 'Proprietary and Confidential' somewhere in footer to denote the confidentiality of proposal information
Should not have
• - cheesy stock images

```html
<!DOCTYPE html>
<html lang="en">
<head>
<meta charset="utf-8">
<title>ARC Project Approach – Wexmoor Lane</title>
<link rel="stylesheet" href="https://fonts.googleapis.com/css2?family=Open+Sans:ital,wght@0,300;0,400;0,600;0,700;1,400&display=swap">
<style>
  :root {
    --brand-blue: #07649c;
    --brand-blue-dark: #0a5a8c;
    --accent-cyan: #45c4f2;
    --heading-blue: #0b64a0;
    --body-grey: #4a4a4a;
    --rule-blue: #9cc3e0;
    --page-bg: #ffffff;
  }
  * { margin: 0; padding: 0; box-sizing: border-box; }
  html, body { width: 1200px; height: 800px; overflow: hidden; background: var(--page-bg); }
  body { font-family: "Open Sans", Arial, sans-serif; color: var(--body-grey); }

  .page { position: relative; width: 1200px; height: 800px; overflow: hidden; }

  .hero-band {
    position: absolute; left: 0; top: 0; width: 508px; height: 213px;
    background: var(--brand-blue); padding: 38px 30px 0 32px;
  }
  .hero-title { color: #fff; font-weight: 600; font-size: 28px; letter-spacing: 0.3px; line-height: 1.1; }
  .hero-quote {
    margin-top: 14px; color: var(--accent-cyan); font-style: italic;
    font-size: 16.2px; line-height: 24px;
  }
  .hero-photo {
    position: absolute; left: 511px; top: 0; width: 689px; height: 213px;
    background: linear-gradient(120deg, #dfe6ea 0%, #c9a58a 40%, #b07a5c 60%, #e4e9ec 100%);
  }

  .intro {
    position: absolute; left: 97px; top: 248px; width: 465px;
    color: var(--heading-blue); font-weight: 300; font-size: 15.2px; line-height: 21px;
    text-align: justify;
  }

  .section-heading {
    position: absolute; color: var(--heading-blue); font-weight: 300; font-size: 22px;
    line-height: 1.2; padding-bottom: 2px; border-bottom: 1px solid var(--heading-blue);
  }
  .heading-discover { left: 97px; top: 345px; }
  .heading-technical { left: 600px; top: 345px; }
  .section-icon { position: absolute; left: 43px; top: 346px; width: 40px; height: 40px; }

  .body-copy {
    position: absolute; font-size: 11.6px; line-height: 20.4px; text-align: justify;
  }
  .body-copy strong { color: var(--heading-blue); font-weight: 700; }
  .discover-copy { left: 97px; top: 394px; width: 465px; }
  .approach-copy { left: 97px; top: 637px; width: 465px; }
  .approach-copy .lead { color: var(--heading-blue); font-weight: 700; font-size: 13.4px; }
  .technical-copy { left: 856px; top: 238px; width: 313px; }

  .accent-block { position: absolute; left: 600px; top: 560px; width: 253px; height: 171px; background: var(--brand-blue); }
  .solution-photo {
    position: absolute; left: 856px; top: 560px; width: 312px; height: 171px;
    background: radial-gradient(ellipse at 60% 45%, #3e8fd0 0%, #14406e 45%, #081a30 100%);
  }

  .footer-rule { position: absolute; top: 777px; height: 1px; background: var(--rule-blue); }
  .rule-left { left: 77px; width: 477px; }
  .rule-right { left: 606px; width: 510px; }
  .footer-page { position: absolute; left: 540px; top: 760px; font-size: 11.6px; color: var(--heading-blue); }
  .footer-url { position: absolute; left: 629px; top: 760px; font-size: 11.6px; color: var(--heading-blue); }
  .footer-mark { position: absolute; top: 757px; display: flex; align-items: center; gap: 4px; }
  .footer-mark .dot { width: 30px; height: 30px; border-radius: 50%; background: var(--brand-blue); }
  .footer-mark .name { font-size: 9px; font-weight: 600; color: var(--brand-blue); line-height: 1; width: 40px; }
  .mark-left { left: 12px; }
  .mark-right { left: 1122px; }
</style>
</head>
<body>
<main class="page">
  <header class="hero-band">
    <h1 class="hero-title">ARC PROJECT APPROACH</h1>
    <p class="hero-quote">“Although specific activities and deliverables will depend on the outcome of our discovery phase and the final creative designs, we propose the following approach to the ARC project. ”</p>
  </header>
  <div class="hero-photo" role="img" aria-label="Photo of many raised hands giving a thumbs-up"></div>

  <p class="intro">We prefer to work in a highly collaborative fashion with our clients to ensure that we’re delivering what you need, when you need it, and within your organization’s budget.</p>

  <svg class="section-icon" viewBox="0 0 40 40" aria-hidden="true">
    <circle cx="20" cy="20" r="20" fill="var(--brand-blue)"/>
    <circle cx="18" cy="18" r="7.5" fill="none" stroke="#fff" stroke-width="3"/>
    <line x1="23.5" y1="23.5" x2="30" y2="30" stroke="#fff" stroke-width="4" stroke-linecap="round"/>
  </svg>
  <h2 class="section-heading heading-discover">DISCOVER &amp; DESIGN</h2>

  <p class="body-copy discover-copy"><strong>Discover:</strong> Our first order of business is to get to know your organization – to learn about how you work, the details of what you’re trying to accomplish online, and how best for us to align technology around your goals. Your Wexmoor Lane team will dive into your needs, goals, current systems, and the problems you’re trying to solve, so that all of our recommendations will fit within your organizational ecosystem and your budget. During the discovery phase, we may use methods such as stakeholder interviews, process evaluation, current data and performance analysis, and design and functional review to build a complete picture of current challenges and how we can help address these to meet your organizational goals. Once we’re thinking like members of your team, we then design both a project approach and a technical solution.</p>

  <p class="body-copy approach-copy">The <span class="lead">PROJECT APPROACH</span> encompasses the working plan that will get our joint teams from conception to launch, including a finalized budget and scope, detailed project timeline, clear-cut areas of responsibility, and communication, sharing, and tracking tools to best facilitate our collaboration. You’ll find more below on tools we typically use.</p>

  <h2 class="section-heading heading-technical">TECHNICAL SOLUTION</h2>

  <p class="body-copy technical-copy">The technical solution is our blueprint for developing and integrating all of the complex pieces of your technology puzzle. Your organization thinks big, and to be successful, you’ll need at a minimum a well-constructed integration with MEMBERDESK, the ARC Digital Library, intuitive content publishing workflows, and pixel-perfect implementation for desktop, mobile and tablet devices. We work together with you and your chosen design firm to architect end-to-end solutions that translate the creative to the functional, map the multi-directional flow of data through systems, and spec out any needed custom development according to your requirements. In addition to documenting our development tasks, our solution will plan for key areas including how (and what) content needs to be migrated and Search Engine Optimization.</p>

  <div class="accent-block"></div>
  <div class="solution-photo" role="img" aria-label="Photo of a businessman touching a glowing on-screen button labelled Solution"></div>

  <footer>
    <div class="footer-mark mark-left"><span class="dot"></span><span class="name">Wexmoor Lane</span></div>
    <div class="footer-rule rule-left"></div>
    <span class="footer-page">Page : 01</span>
    <span class="footer-url">www.wexmoorlane.com</span>
    <div class="footer-rule rule-right"></div>
    <div class="footer-mark mark-right"><span class="dot"></span><span class="name">Wexmoor Lane</span></div>
  </footer>
</main>
</body>
</html>
```